Etikett für Flaschenwein gesucht
Zielgruppe
Weingeschäft -> Verkauf von Flaschenweine; Zielgruppe: Weintrinker, Genusstrinker oder auch jene Personen, die beim Einkaufen einfach gerne eine Flasche Wein mitnehmen wollen und bewusst unsere Weinflasche wählen, da ihnen das Design der Etikette zusagt; !!! Folgeaufträge denkbar!!! für Weinkarten Design, Roll-Up, Autobeschriftungen u.v.m
Aufgabenstellung
Schlicht, elegant und modern; Entwurf einer Weinetikette für exclusive Weine, ev. auch mit dem Namen des Weinguts -> 'Fenzl' eine Marke/ein Logo gestalten bzw. soll auf der Etikette auf alle Fälle Name des Betriebs u. auch die Sorte z.b. 'Weinviertel DAC' ersichtlich sein.
Es gibt momentan Etiketten u. ein Logo aber auf Grund des Betriebsführer-Wechsels (alte Generation übergibt an die neue Generation) kann man hier unvoreingenommen kreativ sein, daher auch kein Upload von bestehenden Dateien.

```html
<!DOCTYPE html>
<html lang="de">
<head>
<meta charset="utf-8">
<title>Fenzl – Weinviertel DAC Etikett</title>
<link href="https://fonts.googleapis.com/css2?family=Fira+Sans:wght@400;500&family=Montserrat:wght@300&family=Merriweather:wght@400&display=swap" rel="stylesheet">
<style>
  :root {
    --paper: #ffffff;
    --copper: #c09069;
    --olive-line: #857758;
    --ink: #111111;
    --sketch-light: #efe9dd;
    --sketch-mid: #d8cdb8;
  }
  html, body {
    margin: 0;
    padding: 0;
    overflow: hidden;
    background: var(--paper);
  }
  .label {
    position: relative;
    width: 878px;
    height: 1200px;
    background: var(--paper);
    overflow: hidden;
  }
  .grape-illustration {
    position: absolute;
    left: 433px;
    top: 0;
    width: 445px;
    height: 834px;
  }
  .brand-name {
    position: absolute;
    left: 26px;
    top: 722px;
    margin: 0;
    font-family: "Fira Sans", sans-serif;
    font-weight: 400;
    font-size: 172px;
    line-height: 1;
    color: var(--copper);
    letter-spacing: 1px;
  }
  .divider {
    position: absolute;
    left: 0;
    top: 921px;
    width: 878px;
    height: 4px;
    background: var(--olive-line);
  }
  .wine-type {
    position: absolute;
    left: 40px;
    top: 935px;
    margin: 0;
    font-family: "Montserrat", sans-serif;
    font-weight: 300;
    font-size: 53px;
    line-height: 1;
    color: var(--ink);
    letter-spacing: 0.5px;
  }
  .description {
    position: absolute;
    left: 41px;
    top: 1030px;
    margin: 0;
    font-family: "Fira Sans", sans-serif;
    font-weight: 400;
    font-size: 28px;
    line-height: 40px;
    color: var(--ink);
    letter-spacing: 0.6px;
  }
  .lot-number {
    position: absolute;
    left: 562px;
    top: 880px;
    margin: 0;
    font-family: "Merriweather", serif;
    font-weight: 400;
    font-size: 330px;
    line-height: 1;
    color: var(--copper);
    letter-spacing: -8px;
  }
</style>
</head>
<body>
  <main class="label">
    <svg class="grape-illustration" role="img" aria-label="Zeichnung einer hängenden Weintraube mit Rebstiel und Weinblättern in Olivbraun" viewBox="0 0 445 834">
      <defs>
        <radialGradient id="grape-tone" cx="0.62" cy="0.68" r="0.6">
          <stop offset="0" stop-color="var(--sketch-mid)"/>
          <stop offset="1" stop-color="var(--sketch-light)"/>
        </radialGradient>
      </defs>
      <path d="M300 0 L350 0 L300 170 L445 430 L445 760 L340 780 L210 834 L120 760 L10 710 L15 600 L80 560 L40 300 L200 180 Z" fill="url(#grape-tone)"/>
    </svg>

    <h1 class="brand-name">Fenzl</h1>
    <div class="divider"></div>
    <h2 class="wine-type">WEINVIERTEL DAC</h2>
    <p class="description">FenzlLorem ipsum dolor sit amet,<br>consectetuer adipiscing elit, sed diam</p>
    <p class="lot-number">01</p>
  </main>
</body>
</html>
```